QRV Business Cards

We are looking for innovative edits to freshen up the card we uploaded. Several examples to choose from will be very helpful. Once we get this decided we will need cards for approximately 20 people.

From the BC attached you will see most of the content we want to keep, we are looking for layout options..the Logo must stay red/blue everything else may be changed to enhance.

Each employee will have their picture on the card.

Target Market(s)

B2B and Government agencies

Industry/Entity Type

Business

Contact Information for Business Card

This is a double sided fold over business card.

Requirements
Must have
• LOGO - same color and format
• LED Lighting Solutions w/Design, Installation, Financing as a stand out
Nice to have
• We had a cartoon charter drawn but I'm not sure if he will fit the card or not...just providing an idea.

```html
<!DOCTYPE html>
<html lang="en">
<head>
<meta charset="utf-8">
<title>QRV Business Card</title>
<link href="https://fonts.googleapis.com/css2?family=Arimo:wght@400;700&family=Tinos&display=swap" rel="stylesheet">
<style>
  :root {
    --bg: #ececec;
    --card: #ffffff;
    --red: #e8283a;
    --blue: #2a6fc0;
    --blue-light: #5a9fe0;
    --sky-top: #3f86e6;
    --sky-bottom: #cfe2fb;
    --shadow: rgba(0,0,0,0.18);
  }
  * { box-sizing: border-box; margin: 0; padding: 0; }
  html, body { width: 1200px; height: 1000px; overflow: hidden; }
  body {
    background: var(--bg);
    font-family: "Arimo", Arial, sans-serif;
    position: relative;
  }
  .card {
    position: absolute;
    left: 337px;
    width: 525px;
    height: 300px;
    background: var(--card);
    box-shadow: 0 3px 10px var(--shadow);
    overflow: hidden;
  }
  .card-front { top: 160px; }
  .card-back { top: 540px; }

  /* Front */
  .swoosh { position: absolute; top: 0; right: 0; width: 140px; height: 300px; }
  .brand {
    position: absolute; left: 36px; top: 72px;
    font-weight: 700; font-size: 64px; color: var(--red); letter-spacing: 2px;
  }
  .portrait {
    position: absolute; right: 82px; top: 28px;
    width: 150px; height: 120px;
    background: linear-gradient(135deg, #d9cfc4, #6b5a4e 70%, #2b2b2b);
  }
  .staff-name {
    position: absolute; right: 82px; top: 158px; text-align: right;
    color: var(--red); font-weight: 700; font-size: 17px;
  }
  .staff-title {
    position: absolute; right: 82px; top: 180px; text-align: right;
    color: var(--red); font-size: 12px;
  }
  .contact {
    position: absolute; left: 36px; bottom: 26px;
    color: var(--blue); font-size: 12.5px; line-height: 1.45; font-style: normal;
  }
  .contact .email { margin-top: 10px; }

  /* Back */
  .hero {
    position: absolute; right: 0; top: 0; width: 190px; height: 300px;
    background: linear-gradient(170deg, var(--sky-top), var(--sky-bottom));
  }
  .text-zone {
    position: absolute; left: 0; top: 0; width: 335px; height: 300px;
    padding: 24px 0 0 24px;
  }
  .headline {
    font-family: "Tinos", "Times New Roman", serif;
    font-weight: 400;
    color: var(--blue); font-size: 22px; letter-spacing: 0.3px;
    white-space: nowrap;
  }
  .pillars {
    margin-top: 6px;
    color: var(--red); font-size: 15px; white-space: nowrap;
  }
  .services {
    margin-top: 18px;
    display: flex; gap: 11px;
  }
  .service-list {
    list-style: none; color: var(--blue-light);
    font-weight: 700; font-size: 11px; line-height: 1.6; white-space: nowrap;
  }
  .service-list.right { color: var(--blue); }
  .divider { width: 1.5px; background: var(--red); }
  .website {
    position: absolute; left: 24px; bottom: 18px;
    color: var(--red); font-weight: 700; font-size: 20px; white-space: nowrap;
  }
</style>
</head>
<body>
  <section class="card card-front">
    <svg class="swoosh" viewBox="0 0 140 300" aria-hidden="true">
      <path d="M60 0 Q120 70 140 150 L140 0 Z" fill="var(--red)"/>
      <path d="M46 0 Q108 70 130 160 L140 150 Q120 70 60 0 Z" fill="var(--blue)"/>
      <path d="M34 0 Q98 70 122 170 L130 160 Q108 70 46 0 Z" fill="#ffffff"/>
    </svg>
    <div class="brand">QRV</div>
    <div class="portrait" role="img" aria-label="Employee portrait photo"></div>
    <div class="staff-name">Daniel Harper</div>
    <div class="staff-title">Chief Executive Officer</div>
    <address class="contact">
      <div>415 B Harbor Rd., Millbrook, MD 21000</div>
      <div>Office | 800-555-0142 x214</div>
      <div>Mobile | 410-555-0187</div>
      <div>Fax | 800-555-0143</div>
      <div class="email">DHarper@QRVLighting.com</div>
    </address>
  </section>

  <section class="card card-back">
    <div class="hero" role="img" aria-label="Cartoon superhero mascot flying on a blue sky"></div>
    <div class="text-zone">
      <h1 class="headline">LED LIGHTING SOLUTIONS</h1>
      <div class="pillars">Design &#9733; Installation &#9733; Financing</div>
      <div class="services">
        <ul class="service-list">
          <li>Roadway Lighting</li>
          <li>Sign Services</li>
          <li>Sports Lighting</li>
          <li>Stray Voltage Testing</li>
          <li>Traffic Signals</li>
          <li>Utility Locating</li>
          <li>Vacuum Excavation</li>
        </ul>
        <span class="divider"></span>
        <ul class="service-list right">
          <li>24 Hour Emergency Service</li>
          <li>Directional Drilling</li>
          <li>Electrical Services</li>
          <li>Energy Audits</li>
          <li>Night Inspections</li>
          <li>Parking Lot Lighting</li>
          <li>Pole Inspections</li>
        </ul>
      </div>
      <div class="website">www.QRVLighting.com</div>
    </div>
  </section>
</body>
</html>
```